Mavro Scrub - Contact/Landing Page

I need a landing page which will essentially be the page that customers will go to from the 'website' link on GMB listing. It will provide a short overview of services which need to be selectable. a little further down can capture some contact details followed by a large Submit Now button etc...

I have some icon/logo's that can be utilised at the bottom of the page as industry type references.

Target Market(s)

End of Lease Cleaning Services

Industry/Entity Type

Cleaning Service

Colors

Designer to choose colors to be used in the design.

Requirements
Must have
• As per description
Should not have
• Colours to match my website mavroscrub.com.au

```html
<!DOCTYPE html>
<html lang="en">
<head>
<meta charset="utf-8">
<title>Mavro Scrub – End of Lease Cleaning</title>
<link href="https://fonts.googleapis.com/css2?family=Crimson+Text:wght@400;700&family=IBM+Plex+Sans:wght@400&family=Roboto:wght@400;500&display=swap" rel="stylesheet">
<style>
:root{
  --blue-deep:#4588c8;
  --blue-mid:#539fd9;
  --blue-light:#5bb8ea;
  --ink:#1c1c1c;
  --white:#ffffff;
  --card-shadow:rgba(0,0,0,.08);
  --field-border:#9ab8d4;
}
*{margin:0;padding:0;box-sizing:border-box}
html,body{width:667px;height:1200px;overflow:hidden;background:var(--white)}
body{position:relative;font-family:"Roboto",sans-serif;color:var(--ink)}
.abs{position:absolute}

/* hero */
.hero{left:0;top:0;width:667px;height:330px;
  background:linear-gradient(160deg,#5d9bd2 0%,#5aa2db 55%,#5fb3e6 100%)}
.top-contact{left:56px;top:9px;color:var(--white);display:flex;align-items:center;gap:6px}
.top-contact svg{width:22px;height:22px}
.top-contact .line1{font-size:8.5px;letter-spacing:.1px}
.top-contact .line2{font-size:9.5px;font-weight:500;margin-top:2px}
.btn-quote-top{left:529px;top:9px;width:82px;height:24px;border:1px solid var(--white);
  color:var(--white);font-size:8.5px;font-weight:500;display:flex;align-items:center;justify-content:center}
.brand{left:0;width:667px;top:110px;text-align:center;font-family:"Crimson Text",serif;
  font-weight:700;font-size:46px;line-height:1;color:var(--white);letter-spacing:1px}
.brand-mark{left:313px;top:52px;width:40px;height:40px;border-radius:50%;background:var(--white);opacity:.9}
.tagline{left:0;width:667px;top:266px;text-align:center;font-family:"Crimson Text",serif;
  font-size:21px;color:var(--white)}
.tagline span{margin:0 12px}

/* services */
.section-title{left:0;width:667px;text-align:center;font-family:"Crimson Text",serif;
  font-weight:700;font-size:23px;color:var(--ink)}
.card{top:425px;width:176px;height:174px;background:var(--white);
  box-shadow:0 0 6px var(--card-shadow);text-align:center;color:var(--ink)}
.card.selected{background:linear-gradient(180deg,var(--blue-deep),var(--blue-light));color:var(--white)}
.card .icon{width:42px;height:42px;margin:14px auto 0;border-radius:4px;background:#cfe4f5}
.card.selected .icon{background:rgba(255,255,255,.35)}
.card h3{font-family:"Crimson Text",serif;font-weight:400;font-size:21px;margin-top:7px;line-height:1.2}
.card p{font-family:"IBM Plex Sans",sans-serif;font-size:10px;line-height:15.6px;margin:5px 12px 0;height:47px}
.card .select{font-size:8.5px;font-weight:500;color:var(--blue-mid);display:flex;
  align-items:center;justify-content:center;gap:5px;margin-top:6px}
.card.selected .select{color:var(--white)}
.select svg{width:9px;height:9px}

/* quote */
.quote{left:0;top:652px;width:667px;height:329px;
  background:linear-gradient(180deg,var(--blue-deep),var(--blue-light))}
.quote-photo{left:0;top:652px;width:667px;height:329px}
.quote h2{left:57px;top:708px;font-family:"Crimson Text",serif;font-weight:700;font-size:23px;color:var(--white)}
.field-label{left:59px;font-size:9px;color:var(--white)}
.field{left:115px;width:194px;height:25px;background:var(--white);border:1px solid var(--field-border)}
.btn-submit{left:117px;top:901px;width:74px;height:26px;border:1px solid var(--white);
  color:var(--white);font-size:9px;font-weight:500;display:flex;align-items:center;justify-content:center}
.contact-email{left:205px;top:902px;color:var(--white);font-size:9px;font-weight:500;line-height:12px}

/* clients */
.client{top:1070px;height:34px}

/* footer */
.footer{left:0;top:1162px;width:667px;height:38px;background:linear-gradient(90deg,var(--blue-deep),var(--blue-mid));
  color:var(--white)}
.footer .copy{left:56px;top:14px;font-size:8.5px}
.footer .social{left:322px;top:7px;width:24px;height:24px;border:1px solid var(--white);border-radius:50%}
.footer .licence{right:56px;top:12px;font-size:10px}
</style>
</head>
<body>

<div class="abs hero" role="img" aria-label="Soft blue-tinted photo of a cleaner spraying in a bright living room"></div>
<div class="abs top-contact">
  <svg viewBox="0 0 24 24" fill="none" stroke="#fff" stroke-width="1.5"><path d="M6 3l3 4-2 2c1 2 3 4 5 5l2-2 4 3-2 3c-6 0-12-6-12-12z"/></svg>
  <div><div class="line1">HOUSE CLEANING AND PEST CONTROL</div><div class="line2">CALL / SMS 0491 570 156</div></div>
</div>
<div class="abs btn-quote-top">GET A QUOTE</div>
<div class="abs brand-mark"></div>
<div class="abs brand">MAVRO SCRUB</div>
<div class="abs tagline">End of Lease Cleaning<span>|</span>Licensed Pest Control</div>

<h2 class="abs section-title" style="top:383px">WHAT WE DO</h2>

<div class="abs card" style="left:55px">
  <div class="icon" role="img" aria-label="Cleaning tools icon"></div>
  <h3>Cleaning</h3>
  <p>All interior cleaning carried out to property management requirements</p>
  <div class="select">SELECT <svg viewBox="0 0 10 10"><rect x=".5" y=".5" width="9" height="9" fill="none" stroke="currentColor"/></svg></div>
</div>
<div class="abs card selected" style="left:246px">
  <div class="icon" role="img" aria-label="Carpet cleaning icon"></div>
  <h3>Carpet Cleaning</h3>
  <p>Carpet stacam cleaning to Australian Standard As 3733:1995</p>
  <div class="select">SELECT <svg viewBox="0 0 10 10"><rect x=".5" y=".5" width="9" height="9" fill="none" stroke="currentColor"/><path d="M2 5l2 2 5-6" fill="none" stroke="currentColor"/></svg></div>
</div>
<div class="abs card" style="left:435px">
  <div class="icon" role="img" aria-label="Pest control sprayer icon"></div>
  <h3>Pest Control</h3>
  <p>Mandatory requirement for pets on premises</p>
  <div class="select">SELECT <svg viewBox="0 0 10 10"><rect x=".5" y=".5" width="9" height="9" fill="none" stroke="currentColor"/></svg></div>
</div>

<div class="abs quote"></div>
<svg class="abs quote-photo" viewBox="0 0 667 329" role="img" aria-label="Photo of a pest control technician in overalls holding a sprayer">
  <defs><linearGradient id="photoTone" x1="0" y1="0" x2="1" y2="0">
    <stop offset="0" stop-color="#5a3a2c"/><stop offset=".45" stop-color="#4a6fae"/><stop offset=".75" stop-color="#dcdad6"/><stop offset="1" stop-color="#e6e4e0"/></linearGradient></defs>
  <polygon points="355,0 667,0 667,329 310,329" fill="url(#photoTone)"/>
</svg>
<h2 class="abs" style="left:57px;top:708px;font-family:'Crimson Text',serif;font-weight:700;font-size:23px;color:#fff">GET A QUOTE</h2>

<div class="abs field-label" style="top:753px">First Name*</div><div class="abs field" style="top:746px"></div>
<div class="abs field-label" style="top:784px">sur Name*</div><div class="abs field" style="top:776px"></div>
<div class="abs field-label" style="top:814px">Email*</div><div class="abs field" style="top:807px"></div>
<div class="abs field-label" style="top:845px">Phone*</div><div class="abs field" style="top:837px"></div>
<div class="abs field-label" style="top:875px">Suburb*</div><div class="abs field" style="top:868px"></div>
<div class="abs btn-submit">SUBMIT</div>
<div class="abs contact-email">Email<br>info@mavroscrub.com.au</div>

<h2 class="abs section-title" style="top:1027px">OUR CLIENTS</h2>
<div class="abs client" style="left:53px;width:84px;background:#2b2b2b;border-radius:3px"></div>
<div class="abs client" style="left:180px;width:101px;background:#c0404a;border-radius:3px;opacity:.85"></div>
<div class="abs client" style="left:332px;width:58px;background:#1f4b8f;border-radius:3px"></div>
<div class="abs client" style="left:422px;width:106px;height:31px;top:1072px;background:#8fbf3a"></div>
<div class="abs client" style="left:554px;width:58px;background:#12396b;border-radius:3px"></div>

<div class="abs footer">
  <div class="abs copy">© 2021 Mavro Scrub. All Rights Reserved</div>
  <div class="abs social"></div>
  <div class="abs licence">PEST LICENCE: 5170342</div>
</div>

</body>
</html>
```